Visitenkarten
Zielgruppe
Wir handeln und restaurieren (mit) sehr hochwertigen Fahrzeugen (Oldtimier/Supercars) bis in den Bereich von mehreren Millionen Euro. Die Zielgruppe sind potentielle Käufer im sehr gehobenen Premium Segment.
Aufgabenstellung
Eine Visitenkarte im Idealfall mit dem schwarzen Logo soll erstellt werden. Standardformat oder ein kreatives, aber praktikables Format. Ziel ist eine sehr hochwertige, geprägte Visitenkarte. Frontseite das Velvet Marques Logo, Rückseite einmal: Jonas Wehrberg, Owner, Phone +436601742863, Email Sales@velvet-marques.com Arlenburg Morvanik (generisch anpassbare Adresse)

```html
<!DOCTYPE html>
<html lang="de">
<head>
<meta charset="utf-8">
<title>Visitenkarte – Rückseite</title>
<link rel="stylesheet" href="https://fonts.googleapis.com/css2?family=Felipa&display=swap">
<style>
  :root {
    --gold-left: #9c6d2e;
    --gold-right: #ca9418;
    --ink: #0c0a06;
    --ink-shadow: rgba(0, 0, 0, 0.35);
  }
  html, body {
    margin: 0;
    padding: 0;
    width: 1200px;
    height: 1200px;
    overflow: hidden;
  }
  .card-back {
    position: relative;
    width: 1200px;
    height: 1200px;
    background: linear-gradient(90deg, var(--gold-left) 0%, var(--gold-right) 100%);
    font-family: "Felipa", cursive;
    color: var(--ink);
    text-shadow: 0 3px 6px var(--ink-shadow);
  }
  .contact-line {
    position: absolute;
    left: 0;
    right: 0;
    margin: 0;
    text-align: center;
    font-size: 82px;
    line-height: 1;
    font-style: italic;
    white-space: nowrap;
  }
  .owner   { top: 290px; }
  .phone   { top: 393px; }
  .email   { top: 497px; }
  .address-label { top: 604px; }
  .address { top: 798px; }
</style>
</head>
<body>
  <main class="card-back">
    <p class="contact-line owner">Inhaber: Jonas Wehrberg, Owner</p>
    <p class="contact-line phone">Phone : +436601742863</p>
    <p class="contact-line email">Email : Sales@velvet-marques.com</p>
    <p class="contact-line address-label">Adresse:</p>
    <p class="contact-line address">Arlenburg Morvanik</p>
  </main>
</body>
</html>
```